依頼詳細
①高校受験専門、②ウィークリーテストを行っている理由、③授業を受けるだけではいけない、④テスト期間は何回でも通塾可能といった碧陽舎ならではの部分を強く打ち出していけたらと考えております。

学年末テストのタイミング(2月中旬から3月にかけて予定)で、新聞折込やポスティングを考えております。

小学生、中1、中2の塾生に男の子が多いこともあり、特に女子生徒を持つご家庭に響くようなチラシデザインだとありがたいです!

授業風景の写真も出来るだけ使ってください!
記載項目
学習塾碧陽舎/〒318-0627 栃木県下野市梅ノ木町41-7/電話0285-61-4893/ホームページhttps://www.hekiyousha-example.net/本気で成績を上げたい子のための学習塾/料金などは付属のファイルから

塾説明会日程
3月4日(日)15:00~  3月10日(土)15:00~  3月21日(水/祝)15:00~  3月24日(土)15:00~  3月31日(土)15:00~
時間は45分ほどを想定しています。事前にご予約のお電話をお願い申し上げます。
説明会にご参加頂いた方は、入塾金10,800円を無料とさせていただきます!
サイズ
B4
ページ数
両面
希望イメージ
シンプル 複雑
単色 カラフル
暗い 明るい
日常 高級
遊び心 厳粛
未来的 伝統的
女性的 男性的
希望する色
赤系
納品ファイル
• 高解像度JPG (.jpg)
補足説明
開校一周年の部分を強調頂けると嬉しいです!
■ 選んだ理由

見出しの打ち出し方と表面にシンプルでありつつも情報量の多いところが気に入りました!

■ 提案者全員のお礼・コメント

たくさんのご提案ありがとうございました。

たくさん悩んだ末の決断でした。また夏の募集の時期などにチラシの作成をお願いすることあるかと思うので、その際にはよろしくお願いいたします!

```html
<!DOCTYPE html>
<html lang="ja">
<head>
<meta charset="utf-8">
<title>学習塾碧陽舎 開校1周年 説明会のご案内</title>
<link rel="stylesheet" href="https://fonts.googleapis.com/css2?family=Noto+Sans+JP:wght@400;500;700;900&family=M+PLUS+Rounded+1c:wght@700;800;900&display=swap">
<style>
:root{
  --red:#d9232e;
  --red-dark:#b3121c;
  --pink:#fde6e8;
  --pink-mid:#f7c6cb;
  --ink:#333333;
  --muted:#666666;
  --white:#ffffff;
  --photo-a:#cfd9e3;
  --photo-b:#e9d8c8;
}
*{margin:0;padding:0;box-sizing:border-box}
html,body{width:848px;height:1200px;overflow:hidden;background:var(--white)}
body{font-family:"Noto Sans JP",sans-serif;color:var(--ink);position:relative}
.flyer{position:relative;width:848px;height:1200px;overflow:hidden}

/* header */
.site-header{position:absolute;left:0;top:0;width:848px;height:80px;display:flex;align-items:center;padding:0 28px;border-bottom:4px solid var(--red)}
.brand{display:flex;align-items:center;gap:10px}
.brand-mark{width:34px;height:34px;background:var(--red)}
.brand-name{font-family:"Noto Sans JP",sans-serif;font-weight:900;font-size:34px;color:var(--red);letter-spacing:2px}
.brand-label{font-size:12px;font-weight:700;color:var(--red);writing-mode:vertical-rl;margin-right:-4px}
.anniversary{margin-left:70px;font-family:"M PLUS Rounded 1c",sans-serif;font-weight:900;font-size:34px;color:var(--red);letter-spacing:3px}
.anniversary b{font-size:54px;vertical-align:-4px;margin:0 4px}

/* hero */
.hero{position:absolute;left:0;top:84px;width:848px;height:342px}
.hero-photo{position:absolute;inset:0;background:linear-gradient(110deg,var(--photo-a) 0%,#e8eef3 45%,var(--photo-b) 100%)}
.hero-message{position:absolute;left:28px;top:22px;width:400px;padding:18px 22px;background:rgba(217,35,46,.88);color:var(--white)}
.hero-message h2{font-size:19px;font-weight:700;margin-bottom:10px;letter-spacing:1px}
.hero-message p{font-size:12.5px;line-height:1.8}
.hero-message .sign{text-align:right;margin-top:8px;font-size:12px}

/* banner */
.concept{position:absolute;left:0;top:430px;width:848px;height:92px;background:var(--red);display:flex;align-items:center;justify-content:center}
.concept-title{background:var(--white);border-radius:46px;padding:4px 54px;font-family:"M PLUS Rounded 1c",sans-serif;font-weight:900;font-size:52px;color:var(--red);letter-spacing:4px}

/* points */
.points{position:absolute;left:22px;top:532px;width:804px;display:grid;grid-template-columns:1fr 1fr;gap:10px 14px}
.point{height:108px;border:2px solid var(--red);background:var(--white);display:flex;flex-direction:column}
.point-head{display:flex;align-items:center;background:var(--pink);border-bottom:1px solid var(--pink-mid)}
.point-num{background:var(--red);color:var(--white);font-weight:700;font-size:12px;padding:4px 8px;font-family:"M PLUS Rounded 1c",sans-serif}
.point-title{color:var(--red);font-weight:700;font-size:14px;padding-left:8px}
.point-body{display:flex;gap:8px;padding:6px 8px;flex:1}
.point-body p{font-size:11px;line-height:1.6;flex:1}
.point-photo{width:104px;height:66px;background:linear-gradient(135deg,var(--photo-a),var(--photo-b));flex:none}

/* sessions */
.sessions{position:absolute;left:22px;top:898px;width:440px}
.sessions-title{display:inline-block;background:var(--red);color:var(--white);font-family:"M PLUS Rounded 1c",sans-serif;font-weight:900;font-size:30px;line-height:42px;padding:0 18px;letter-spacing:3px}
.date-list{display:grid;grid-template-columns:1fr 1fr;gap:2px 14px;margin-top:8px;list-style:none}
.date-list li{font-family:"M PLUS Rounded 1c",sans-serif;font-weight:800;font-size:28px;line-height:36px;height:38px;color:var(--red);display:flex;align-items:center;gap:6px;border-bottom:1px dashed var(--pink-mid)}
.date-list .dow{display:inline-flex;align-items:center;justify-content:center;width:26px;height:26px;border-radius:50%;background:var(--red);color:var(--white);font-size:12px;line-height:1}
.date-list .dow.wide{width:38px;border-radius:13px}
.date-list .time{color:var(--ink);font-size:22px}

.future{position:absolute;left:480px;top:896px;width:346px;height:186px;background:var(--pink);border-radius:6px;padding:14px 14px}
.future h3{font-family:"M PLUS Rounded 1c",sans-serif;font-weight:900;font-size:22px;color:var(--red);margin-bottom:8px}
.future p{font-size:11px;line-height:1.7;width:212px}
.fee-badge{position:absolute;right:8px;top:58px;width:112px;height:112px;border-radius:50%;background:var(--red);color:var(--white);display:flex;flex-direction:column;align-items:center;justify-content:center;text-align:center;line-height:1.25}
.fee-badge small{font-size:10px}
.fee-badge strong{font-size:16px}
.fee-badge em{font-style:normal;font-size:22px;font-weight:900}

/* footer */
.site-footer{position:absolute;left:0;top:1096px;width:848px;height:104px;border-top:4px solid var(--red);display:flex;align-items:center;padding:0 28px;gap:22px}
.footer-info{font-size:11.5px;line-height:1.7}
.footer-info .tagline{color:var(--red);font-weight:700;font-size:13px}
.footer-phone{margin-left:auto;display:flex;align-items:center;gap:10px;color:var(--red);font-family:"M PLUS Rounded 1c",sans-serif;font-weight:900;font-size:44px;letter-spacing:1px}
</style>
</head>
<body>
<main class="flyer">

  <header class="site-header">
    <div class="brand">
      <span class="brand-label">学習塾</span>
      <span class="brand-mark"></span>
      <span class="brand-name">碧陽舎</span>
    </div>
    <p class="anniversary">開校<b>1</b>周年</p>
  </header>

  <section class="hero">
    <div class="hero-photo" role="img" aria-label="ランドセルを背負った笑顔の小学生の女の子と男の子の写真"></div>
    <div class="hero-message">
      <h2>碧陽舎塾長の想い</h2>
      <p>碧陽舎は開校から一年、本気で成績を上げたい子どもたちと向き合ってきました。授業を受けるだけでは力はつきません。自分で考え、解き、確かめる時間こそが大切です。毎週のテストで理解度を確かめ、つまずきをその場で解消します。</p>
      <p>女の子も男の子も安心して通える、落ち着いた学習環境を整えています。高校受験まで、一人ひとりに寄り添って全力でサポートします。</p>
      <p class="sign">碧陽舎 塾長</p>
    </div>
  </section>

  <section class="concept">
    <h1 class="concept-title">碧陽舎ってこんな塾!</h1>
  </section>

  <section class="points">
    <article class="point">
      <div class="point-head"><span class="point-num">ポイント1</span><h3 class="point-title">少人数・定員制で細やかな指導</h3></div>
      <div class="point-body"><p>一クラスの人数を限定し、一人ひとりの理解度に合わせて丁寧に指導します。質問しやすい雰囲気です。</p><div class="point-photo" role="img" aria-label="少人数授業の様子の写真"></div></div>
    </article>
    <article class="point">
      <div class="point-head"><span class="point-num">ポイント2</span><h3 class="point-title">毎週のテストで学力を確認</h3></div>
      <div class="point-body"><p>ウィークリーテストで学んだ内容の定着を確認。苦手をためずにすぐに復習できます。</p><div class="point-photo" role="img" aria-label="テストに取り組む生徒の写真"></div></div>
    </article>
    <article class="point">
      <div class="point-head"><span class="point-num">ポイント3</span><h3 class="point-title">自由に自習室の利用が可能</h3></div>
      <div class="point-body"><p>授業を受けるだけでは終わりません。自習室でいつでも学習でき、講師にも質問できます。</p><div class="point-photo" role="img" aria-label="自習室で勉強する生徒の写真"></div></div>
    </article>
    <article class="point">
      <div class="point-head"><span class="point-num">ポイント4</span><h3 class="point-title">充実のテスト対策</h3></div>
      <div class="point-body"><p>定期テスト期間は何回でも通塾可能。学校別の対策で得点アップを目指します。</p><div class="point-photo" role="img" aria-label="テスト対策授業の写真"></div></div>
    </article>
    <article class="point">
      <div class="point-head"><span class="point-num">ポイント5</span><h3 class="point-title">女子生徒も安心の環境</h3></div>
      <div class="point-body"><p>明るく清潔な教室と落ち着いた雰囲気で、女の子も安心して勉強に集中できます。</p><div class="point-photo" role="img" aria-label="教室で学ぶ女子生徒の写真"></div></div>
    </article>
    <article class="point">
      <div class="point-head"><span class="point-num">ポイント6</span><h3 class="point-title">地域密着・高校受験専門</h3></div>
      <div class="point-body"><p>地域の高校入試を知り尽くした講師が、志望校合格まで責任を持って指導します。</p><div class="point-photo" role="img" aria-label="講師が指導する授業風景の写真"></div></div>
    </article>
  </section>

  <section class="sessions">
    <h2 class="sessions-title">説明会開催</h2>
    <ul class="date-list">
      <li>3/4<span class="dow">日</span><span class="time">15:00~</span></li>
      <li>3/10<span class="dow">土</span><span class="time">15:00~</span></li>
      <li>3/21<span class="dow wide">水祝</span><span class="time">15:00~</span></li>
      <li>3/24<span class="dow">土</span><span class="time">15:00~</span></li>
      <li>3/31<span class="dow">土</span><span class="time">15:00~</span></li>
    </ul>
  </section>

  <aside class="future">
    <h3>未来の塾生へ</h3>
    <p>説明会は45分ほどを予定しています。事前にお電話でご予約をお願いいたします。お気軽にご参加ください。</p>
    <div class="fee-badge">
      <small>説明会参加で</small>
      <strong>入塾金</strong>
      <span>10,800円</span>
      <em>無料</em>
    </div>
  </aside>

  <footer class="site-footer">
    <div class="brand">
      <span class="brand-mark"></span>
      <span class="brand-name">碧陽舎</span>
    </div>
    <div class="footer-info">
      <p class="tagline">本気で成績を上げたい子のための学習塾</p>
      <p>〒318-0627 栃木県下野市梅ノ木町41-7</p>
      <p>https://www.hekiyousha-example.net/</p>
    </div>
    <div class="footer-phone">
      <svg width="38" height="38" viewBox="0 0 24 24" aria-hidden="true"><path fill="currentColor" d="M6.6 10.8a15.1 15.1 0 0 0 6.6 6.6l2.2-2.2c.3-.3.7-.4 1-.2 1.1.4 2.3.6 3.6.6.6 0 1 .4 1 1V20c0 .6-.4 1-1 1A17 17 0 0 1 3 4c0-.6.4-1 1-1h3.5c.6 0 1 .4 1 1 0 1.3.2 2.5.6 3.6.1.3 0 .7-.2 1z"/></svg>
      <span>0285-61-4893</span>
    </div>
  </footer>

</main>
</body>
</html>
```